We are working with a new commercial flooring contractor in California. They work on schools, hospitals, and government projects.
A few websites for inspiration:
https://plainrockcoverings.com (These guys are competitors and provide the same work our client does).
https://tjtilework.com (Although NOT a contractor, the simplicity of this site is stunning).
https://www.quietlantern.com (NOT a flooring contractor, but this site is modern, and has a boldness to it).
https://www.sagemeadowatelier.com/en-us (website for an Architectural office that is clean and showcases their work. I can see this working for a flooring contractor).
Thank you for taking the time to consider designing a website for us. We are web developers based in Stockton, CA, USA. Most of our projects go through the same process. Understanding this process may help you win a project with us. We custom-code all of our websites in-house. We don’t have any requirements as to what tools you use for your design, but we ask that you follow these guidelines.
IMAGES:
If you use any images or icons in the design, we ask that you have a link to the asset so we can purchase the image/icon. Most of the designs we submit do not have the customer’s images on them unless they have some great images. Be creative; show us the feeling you are trying to portray with your image choices. Use any royalty-free site you choose. We subscribe to Kestral and mainly use their images, but we can purchase images outside of Kestral.
FONTS:
We ask that you identify the fonts you’re using in the design. This can be done in a message if you want. We typically use Vantor Fonts and Kestral Fonts.
CONTENT:
We're always open to different content and ideas. We often submit designs with stock images so the client can see our vision. We typically take pictures after the website launch to use their images with our vision. Lorem Ipsum is fine for paragraphs, but we ask that you make the Headers with correct English. We want to be able to show the vision and identify the sections of the website.
INSPIRATION:
We typically add a couple of links in the brief of websites we like to help you get started in your design.
REVISIONS:
We do not often ask for revisions of the designs unless we see something in the design that may not appeal to the client. If there are slight changes that we want to make, we do that in the development process.
FEEDBACK:
We rarely give feedback on designs during the design process. We are working on many website projects and do not have the time to provide feedback. We usually respond if your request is well thought out and asks specific questions, but a note asking “feedback, please” usually goes unanswered.

```html
<!DOCTYPE html>
<html lang="en">
<head>
<meta charset="utf-8">
<title>Stonebay Floors — Commercial Flooring</title>
<link href="https://fonts.googleapis.com/css2?family=Jost:wght@400;500;600;700&family=Montserrat:wght@400;500;600;700&display=swap" rel="stylesheet">
<style>
:root{
  --coral:#ec5f5a;
  --red:#e9514d;
  --ink:#222222;
  --muted:#666666;
  --page:#efefef;
  --panel:#e5e5e5;
  --dark:#2d2d2d;
  --white:#ffffff;
}
*{margin:0;padding:0;box-sizing:border-box}
html,body{width:1200px;height:1000px;overflow:hidden}
body{background:var(--coral);font-family:"Montserrat",sans-serif;color:var(--ink);position:relative}
.site{position:absolute;left:462px;top:0;width:276px;height:1000px;background:var(--page);overflow:hidden}
.abs{position:absolute}
/* nav */
.nav{left:0;top:0;width:276px;height:20px;background:var(--white)}
.brand{left:34px;top:4px;display:flex;align-items:center;gap:2px;font-family:"Jost",sans-serif;font-weight:600;font-size:5px;color:var(--ink)}
.brand-dot{width:10px;height:10px;border-radius:50%;background:var(--red)}
.menu{left:143px;top:8px;display:flex;gap:8px;font-size:3.4px;font-weight:600;letter-spacing:.1px}
.btn{background:var(--red);color:var(--white);font-size:3.4px;font-weight:600;display:flex;align-items:center;justify-content:center;border-radius:1px}
.nav-btn{left:226px;top:6px;width:25px;height:8px}
/* hero */
.hero{left:0;top:20px;width:276px;height:138px;background:linear-gradient(90deg,#8d7b68 0%,#c9bfb1 20%,#e2e4e3 45%,#d9dad8 60%,#a9a39b 80%,#6f675e 100%)}
.hero-floor{left:0;top:95px;width:276px;height:43px;background:linear-gradient(180deg,#cdb79c,#a88d6f)}
.hero-card{left:100px;top:38px;width:76px;height:65px;background:rgba(255,255,255,.55);text-align:center;padding-top:22px}
.hero-title{font-family:"Jost",sans-serif;font-weight:700;font-size:8.5px;line-height:1}
.hero-sub{font-family:"Jost",sans-serif;font-weight:400;font-size:8.5px;line-height:1.3}
.hero-text{font-size:3px;line-height:1.4;color:#333;margin:2px 8px 0}
/* stats */
.stats{left:16px;top:151px;width:246px;height:35px;background:var(--dark);display:flex;justify-content:space-around;align-items:center;color:var(--white);text-align:center;padding:0 12px}
.stat-num{font-weight:700;font-size:6px}
.stat-label{font-size:3.3px;font-weight:500}
/* sections */
.eyebrow{font-size:3px;letter-spacing:.6px;color:var(--red);font-weight:500}
.heading{font-family:"Jost",sans-serif;font-weight:500;font-size:10px}
.para{font-size:3.4px;line-height:1.75;color:var(--muted)}
.about-panel{left:160px;top:216px;width:116px;height:100px;background:var(--panel)}
.about-photo{left:139px;top:225px;width:122px;height:81px;background:linear-gradient(135deg,#efe9e0,#cfc5b5 50%,#8b7a66)}
.center{text-align:center;width:276px;left:0}
.tile{width:110px;height:100px}
.tile-label{position:absolute;bottom:0;left:32px;width:47px;height:15px;background:var(--page);font-family:"Jost",sans-serif;font-size:4.5px;font-weight:500;display:flex;align-items:center;justify-content:center;letter-spacing:.2px}
.cta{left:0;top:651px;width:276px;height:114px;background:linear-gradient(90deg,#c9c3bb,#9e968c 30%,#d8d5d0 60%,#c2c0bb)}
.cta-circle{left:144px;top:654px;width:108px;height:108px;border-radius:50%;background:var(--red);color:var(--white);text-align:center;font-family:"Jost",sans-serif;padding-top:30px}
.cta-1{font-size:9px;line-height:1.1}
.cta-2{font-size:12px;font-weight:700;line-height:1.1}
.cta-3{font-size:9px;line-height:1.1}
.cta-text{font-family:"Montserrat",sans-serif;font-size:3px;line-height:1.8;margin:4px 20px 0}
.field{left:63px;top:846px;width:115px;height:10px;background:var(--white);font-size:3px;color:#999;display:flex;align-items:center;padding-left:5px;border-radius:2px 0 0 2px}
.sub-btn{left:178px;top:846px;width:35px;height:10px;border-radius:0 2px 2px 0}
/* footer */
.footer{left:0;top:893px;width:276px;height:107px;background:var(--dark);color:var(--white)}
.foot-text{font-size:3.2px;line-height:1.7;color:#bbb}
.foot-links{font-size:3.6px;line-height:2;color:var(--white)}
.contact-row{display:flex;gap:3px;align-items:flex-start;font-size:3.4px;line-height:1.6;margin-bottom:2px}
.social{display:flex;gap:2px;align-items:center;font-size:3.4px}
.social span.c{width:4px;height:4px;border-radius:50%;background:var(--white);display:inline-block}
.foot-rule{left:0;top:989px;width:276px;height:1px;background:#444}
.copyright{left:0;top:993px;width:276px;text-align:center;font-size:3px;color:#bbb}
</style>
</head>
<body>
<main class="site">
  <header class="abs nav">
    <div class="abs brand"><span class="brand-dot"></span>Stonebay Floors</div>
    <nav class="abs menu"><span>HOME</span><span>ABOUT</span><span>SERVICES</span><span>WORKS</span></nav>
    <a class="abs btn nav-btn">CONTACT US</a>
  </header>

  <section class="abs hero" role="img" aria-label="Bright modern living room with light wood floor, grey sofa and large windows"></section>
  <div class="abs hero-floor" role="img" aria-label="Light oak plank floor"></div>
  <div class="abs hero-card">
    <div class="hero-title">BETTER FLOOR</div>
    <div class="hero-sub">BETTER FUTURE</div>
    <p class="hero-text">Lorem ipsum dolor sit amet consectetur. Aenean volutpat viverra augue malesuada vitae in.</p>
  </div>

  <div class="abs stats">
    <div><div class="stat-num">2000+</div><div class="stat-label">PROJECTS</div></div>
    <div><div class="stat-num">15+</div><div class="stat-label">YEARS EXPERIENCE</div></div>
    <div><div class="stat-num">890+</div><div class="stat-label">SATISFIED CUSTOMERS</div></div>
    <div><div class="stat-num">20+</div><div class="stat-label">COUNTRY</div></div>
  </div>

  <section class="about">
    <div class="abs eyebrow" style="left:25px;top:222px">ABOUT US</div>
    <h2 class="abs heading" style="left:25px;top:226px">WHO WE ARE</h2>
    <p class="abs para" style="left:25px;top:245px;width:104px">Lorem ipsum dolor sit amet consectetur. Aenean volutpat viverra augue malesuada at. Vitae ut euismod in dictumst, et in sed consequat id nulla dui sapien lacus faucibus. Lorem ipsum dolor sit amet consectetur. Aenean volutpat viverra augue malesuada vitae ut euismod in dictumst, et in sed consequat id nulla dui sapien lacus faucibus.</p>
    <a class="abs btn" style="left:25px;top:292px;width:25px;height:8px">CALL US</a>
    <div class="abs about-panel"></div>
    <div class="abs about-photo" role="img" aria-label="Spacious lobby with polished stone floor and built-in shelving"></div>
  </section>

  <section class="services">
    <div class="abs eyebrow center" style="top:355px">SERVICES</div>
    <h2 class="abs heading center" style="top:360px">WHAT WE OFFER</h2>
    <p class="abs para" style="left:63px;top:375px;width:150px;text-align:center">Lorem ipsum dolor sit amet consectetur. Aenean volutpat viverra augue malesuada ut. Vitae ut euismod in dictumst, et in sed consequat id nulla dui sapien lacus.</p>
    <div class="abs tile" style="left:24px;top:403px;background:linear-gradient(135deg,#8a5a34,#d8cfc4 55%,#f1eee9)" role="img" aria-label="Bathroom with wood vanity and tiled floor"><div class="tile-label">FLOORING</div></div>
    <div class="abs tile" style="left:140px;top:403px;background:linear-gradient(135deg,#6f7680,#c9bba7 50%,#efe2cc)" role="img" aria-label="Worker in boots spreading fresh concrete"><div class="tile-label">CONCRETE</div></div>
    <div class="abs tile" style="left:24px;top:512px;background:linear-gradient(160deg,#d9d6d1,#a9a49d 50%,#5b5854)" role="img" aria-label="Hands laying a floor tile on adhesive"><div class="tile-label">TILE</div></div>
    <div class="abs tile" style="left:140px;top:512px;background:linear-gradient(180deg,#e8e6e2,#b9b2a8 45%,#dcd8d2)" role="img" aria-label="Living room with sofa on soft patterned carpet"><div class="tile-label">CARPET</div></div>
  </section>

  <section>
    <div class="abs cta" role="img" aria-label="Flooring installer fitting a tile in a bright room"></div>
    <div class="abs cta-circle">
      <div class="cta-1">Get Your</div>
      <div class="cta-2">Dream Floor</div>
      <div class="cta-3">Now</div>
      <p class="cta-text">Our Flooring Opens The Opportunity For The Floor Of Your Dreams.</p>
    </div>
  </section>

  <section class="newsletter">
    <div class="abs eyebrow center" style="top:801px">NEWSLETTER</div>
    <h2 class="abs heading center" style="top:807px">JOIN TO STAY UPDATED</h2>
    <p class="abs para" style="left:60px;top:823px;width:156px;text-align:center">Lorem ipsum dolor sit amet consectetur. Aenean volutpat viverra augue malesuada at. Vitae ut euismod in dictumst, et in sed consequat id nulla dui sapien lacus faucibus lorem ipsum dolor sit amet.</p>
    <div class="abs field">hello@stonebayfloors.com</div>
    <a class="abs btn sub-btn">SUBSCRIBE</a>
  </section>

  <footer class="abs footer">
    <div class="abs brand" style="left:25px;top:24px;color:var(--white)"><span class="brand-dot"></span>Stonebay</div>
    <p class="abs foot-text" style="left:25px;top:45px;width:60px">Lorem ipsum dolor sit amet consectetur, aliquam nunc mauris porta.</p>
    <div class="abs social" style="left:25px;top:68px"><span>Follow us on</span><span class="c"></span><span class="c"></span><span class="c"></span><span class="c"></span></div>
    <div class="abs foot-links" style="left:101px;top:30px">Home<br>About<br>Service<br>Works<br>Contact</div>
    <div class="abs foot-links" style="left:140px;top:30px">Contact<br>Price Inquiries<br>Shipping &amp; Returns<br>Terms &amp; Conditions<br>FAQ</div>
    <div class="abs" style="left:196px;top:31px;width:56px">
      <div class="contact-row"><svg width="4" height="4" viewBox="0 0 10 10"><path d="M2 1l2 0 1 2.5-1.3 1a5 5 0 0 0 2.8 2.8l1-1.3 2.5 1 0 2c-5 0-9-4-9-9z" fill="#e9514d"/></svg><span>555-014-2290</span></div>
      <div class="contact-row"><svg width="4" height="4" viewBox="0 0 10 10"><rect x="1" y="2" width="8" height="6" fill="#e9514d"/><path d="M1 2l4 3 4-3" stroke="#2d2d2d" fill="none"/></svg><span>hello@stonebayfloors.com</span></div>
      <div class="contact-row"><svg width="4" height="4" viewBox="0 0 10 10"><path d="M5 1a3 3 0 0 1 3 3c0 2-3 5-3 5S2 6 2 4a3 3 0 0 1 3-3z" fill="#e9514d"/></svg><span>12 Harbor Lane, Stockton, CA</span></div>
    </div>
  </footer>
  <div class="abs foot-rule"></div>
  <div class="abs copyright">© All Rights Reserved 2022</div>
</main>
</body>
</html>
```